IT Consulting Business Card Design

We need a business card on our company name....which is a IT consulting and staffing company. We also train masters graduates in various IT courses. 70% of the time these cards will be handed out to the graduate students at the universities. 30% for our clients and business partners. We are uploading our company logo...would like to see something that matches our logo or blends with it. Please visit www.brightvaleworks.com for more details on logo and colors.

Target Market(s)

70% of the time these cards will be handed out to the graduate students at the universities. 30% for our clients and business partners.

Industry/Entity Type

Business

Contact Information for Business Card

Ravi Kondamuri
Vice-President
Bright Vale Works Inc
3807 Morrow Lane, Suite 412
East Brookridge, NJ 07315
ravi@brightvaleworks.com
Office : 1-866-219-3840 X 515
Cell number : 732-581-9034

Requirements
Nice to have
• may be company logo and name on the back of the card and detials on the other side...just a thought..!!

```html
<!DOCTYPE html>
<html lang="en">
<head>
<meta charset="utf-8">
<title>Bright Vale Works – Business Card</title>
<link href="https://fonts.googleapis.com/css2?family=Lato:wght@400;700;900&family=Oswald:wght@600&display=swap" rel="stylesheet">
<style>
  :root {
    --page-bg: #e9e7e4;
    --card-white: #ffffff;
    --brand-red: #e01f26;
    --ink-black: #1b1b1b;
    --ink-dark: #2b2b2b;
    --muted-grey: #9b9b9b;
    --light-grey: #bdbdbd;
  }
  * { box-sizing: border-box; margin: 0; padding: 0; }
  html, body {
    width: 1200px;
    height: 832px;
    overflow: hidden;
    background: var(--page-bg);
    font-family: "Lato", sans-serif;
  }
  .canvas {
    position: relative;
    width: 1200px;
    height: 832px;
  }
  .card {
    position: absolute;
    width: 560px;
    height: 320px;
    background: var(--card-white);
    box-shadow: 0 6px 18px rgba(0,0,0,0.18);
    overflow: hidden;
  }
  .card--front { left: 80px; top: 90px; }
  .card--back  { left: 560px; top: 442px; }

  .front-shapes {
    position: absolute;
    inset: 0;
    width: 100%;
    height: 100%;
  }
  .holder {
    position: absolute;
    right: 28px;
    top: 20px;
    text-align: right;
  }
  .holder__name {
    font-size: 22px;
    font-weight: 400;
    color: var(--ink-black);
    letter-spacing: 0.2px;
  }
  .holder__title {
    font-size: 12px;
    font-weight: 900;
    color: var(--brand-red);
    letter-spacing: 0.6px;
    margin-top: 2px;
  }
  .contact {
    position: absolute;
    right: 28px;
    top: 170px;
    list-style: none;
    text-align: right;
    font-size: 12.5px;
    line-height: 18px;
    color: var(--muted-grey);
    letter-spacing: 0.3px;
  }
  .contact__label { font-weight: 700; color: var(--light-grey); }
  .wordmark {
    font-family: "Oswald", sans-serif;
    font-weight: 600;
    color: var(--brand-red);
    text-transform: uppercase;
    letter-spacing: 0.5px;
    white-space: nowrap;
  }
  .card--front .wordmark {
    position: absolute;
    right: 28px;
    top: 238px;
    font-size: 27px;
  }

  .back-brand {
    position: absolute;
    left: 0;
    right: 0;
    top: 120px;
    display: flex;
    align-items: center;
    justify-content: center;
    gap: 14px;
  }
  .back-brand__dot {
    width: 22px;
    height: 22px;
    border-radius: 50%;
    background: var(--brand-red);
  }
  .card--back .wordmark { font-size: 26px; }
  .address {
    position: absolute;
    left: 0;
    right: 0;
    top: 212px;
    text-align: center;
    font-size: 12.5px;
    color: var(--ink-black);
    letter-spacing: 0.4px;
  }
</style>
</head>
<body>
<main class="canvas">

  <section class="card card--front" aria-label="Card front">
    <svg class="front-shapes" viewBox="0 0 560 320" aria-hidden="true">
      <path d="M0,282 C180,248 360,160 560,58 L560,104 C380,190 200,268 0,300 Z" fill="var(--brand-red)"/>
      <path d="M0,300 C200,268 380,190 560,104 L560,311 L0,311 Z" fill="var(--ink-black)"/>
      <rect x="0" y="311" width="560" height="4" fill="var(--brand-red)"/>
    </svg>

    <header class="holder">
      <h1 class="holder__name">Mr. Ravi Kondamuri</h1>
      <p class="holder__title">VICE-PRESIDENT</p>
    </header>

    <ul class="contact">
      <li><span class="contact__label">cell:</span> 732-581-9034</li>
      <li><span class="contact__label">office:</span> 1-866-219-3840 X 515</li>
      <li><span class="contact__label">email:</span> ravi@brightvaleworks.com</li>
    </ul>

    <p class="wordmark">Bright Vale Works</p>
  </section>

  <section class="card card--back" aria-label="Card back">
    <div class="back-brand">
      <span class="back-brand__dot" aria-hidden="true"></span>
      <p class="wordmark">Bright Vale Works</p>
    </div>
    <p class="address">3807 Morrow Lane, Suite 412 East Brookridge, NJ 07315</p>
  </section>

</main>
</body>
</html>
```